STAND OUT BUSINESS CARD REQUIRED

I would like a business card that is going to be different and stand out!

Target Market(s)

Residential market, adults from 28yrs on

Industry/Entity Type

Electrician

Requirements
Must have
• Business name
• my name
• phone number
• email
• web address
• license no.
• abn
• fax no
• logo
Nice to have
• Extra info:
• FREE quotes
• Fixed pricing
• On time guarantee
• Life time labour Guarantee

```html
<!DOCTYPE html>
<html lang="en">
<head>
<meta charset="utf-8">
<title>Spark Right Electrical – Business Card</title>
<link rel="stylesheet" href="https://fonts.googleapis.com/css2?family=PT+Sans+Narrow:wght@400;700&family=Open+Sans:wght@700&display=swap">
<style>
  :root {
    --paper: #ffffff;
    --ink-grey: #6d6e71;
    --brand-green: #138a46;
    --brand-orange: #e8792a;
    --band-white: #ffffff;
    --art-blue: #a9d8f2;
    --art-green: #2f9a4f;
    --art-red: #b8322a;
  }
  * { margin: 0; padding: 0; box-sizing: border-box; }
  html, body {
    width: 1200px;
    height: 804px;
    overflow: hidden;
    background: var(--paper);
  }
  .card {
    position: relative;
    width: 1200px;
    height: 804px;
    background: var(--paper);
    font-family: "PT Sans Narrow", "Arial Narrow", sans-serif;
  }

  /* Brand block */
  .brand-art {
    position: absolute;
    left: 165px;
    top: 88px;
    width: 280px;
    height: 250px;
    border-radius: 24px;
    background: linear-gradient(160deg, var(--art-blue) 0%, var(--art-green) 55%, var(--art-red) 100%);
    opacity: 0.85;
  }
  .brand-name {
    position: absolute;
    left: 96px;
    top: 352px;
    width: 360px;
    font-weight: 700;
    font-size: 46px;
    line-height: 1.0;
    color: var(--brand-orange);
    text-transform: uppercase;
  }

  /* Identity */
  .person-name {
    position: absolute;
    left: 647px;
    top: 100px;
    font-weight: 700;
    font-size: 47px;
    line-height: 1;
    color: var(--ink-grey);
  }
  .company-name {
    position: absolute;
    left: 648px;
    top: 160px;
    font-size: 40px;
    line-height: 1;
    color: var(--brand-green);
  }
  .company-name .suffix { font-size: 22px; }

  /* Contact list */
  .contact-list {
    position: absolute;
    left: 648px;
    top: 268px;
    list-style: none;
  }
  .contact-row {
    display: flex;
    height: 50px;
    font-size: 40px;
    line-height: 50px;
  }
  .contact-label {
    width: 161px;
    color: var(--brand-green);
  }
  .contact-label .colon { color: var(--ink-grey); font-size: 28px; }
  .contact-value { color: var(--ink-grey); }
  .contact-value.strong { font-weight: 700; }

  /* Guarantee band */
  .promise-band {
    position: absolute;
    left: 0;
    top: 683px;
    width: 1200px;
    height: 121px;
    background: linear-gradient(90deg, #5a2a5e 0%, #6b4699 22%, #2f6fb6 42%, #1eaec9 58%, #76c48a 76%, #5cb85c 100%);
  }
  .promise-list {
    position: absolute;
    top: 14px;
    left: 0;
    width: 1200px;
    text-align: center;
    font-family: "Open Sans", Arial, sans-serif;
    font-weight: 700;
    font-size: 17px;
    letter-spacing: -0.3px;
    color: var(--band-white);
    text-transform: uppercase;
  }
  .promise-list .divider { margin: 0 10px; }
</style>
</head>
<body>
  <div class="card">
    <div class="brand-art" role="img" aria-label="Cartoon electrician superhero flying with a light bulb raised"></div>
    <div class="brand-name">Spark Right Electrical</div>

    <h1 class="person-name">John Doe</h1>
    <p class="company-name">Spark Right Electrical <span class="suffix">Pty Ltd</span></p>

    <ul class="contact-list">
      <li class="contact-row"><span class="contact-label">Tel<span class="colon">:</span></span><span class="contact-value strong">01234567890</span></li>
      <li class="contact-row"><span class="contact-label">Fax<span class="colon">:</span></span><span class="contact-value strong">01234567890</span></li>
      <li class="contact-row"><span class="contact-label">Email<span class="colon">:</span></span><span class="contact-value">john@email.com</span></li>
      <li class="contact-row"><span class="contact-label">Web<span class="colon">:</span></span><span class="contact-value">www.yoursite.com</span></li>
      <li class="contact-row"><span class="contact-label">License No<span class="colon">:</span></span><span class="contact-value">0000000000000000</span></li>
    </ul>

    <div class="promise-band">
      <p class="promise-list">
        Free Quotes<span class="divider">|</span>Fixed Pricing<span class="divider">|</span>On Time Guarantee<span class="divider">|</span>Life Time Labour Guarantee
      </p>
    </div>
  </div>
</body>
</html>
```